Trucking company needs business card design

New trucking company needs fresh ideas on a business card. Contracted exclusively to Parcelwing, can incorporate their colors or style, but not necessary.
Beckley Haulage, Inc (with or without the Inc.)
Dale Quimby, CEO
801-555-0174
PO BOX 672
Cedar Flats, NV

Need to add my email address to the card--beckleyhaulageinc@quillpost.net

Trucking Company

```html
<!DOCTYPE html>
<html lang="en">
<head>
<meta charset="utf-8">
<title>Beckley Haulage, Inc — Business Card</title>
<link rel="stylesheet" href="https://fonts.googleapis.com/css2?family=Audiowide&family=Exo+2:wght@700&family=Josefin+Sans:wght@300;400&display=swap">
<style>
  :root {
    --page: #ece9e4;
    --card-blue: #2176ff;
    --card-deep: #050a1a;
    --silver: #b9c0c8;
    --ink: #0b1020;
    --white: #ffffff;
    --truck-light: #6f8fd6;
    --truck-dark: #1b2f66;
  }
  * { margin: 0; padding: 0; box-sizing: border-box; }
  html, body { width: 1200px; height: 1000px; overflow: hidden; background: var(--page); }
  .canvas { position: relative; width: 1200px; height: 1000px; }

  .card {
    position: absolute;
    width: 700px;
    height: 410px;
    overflow: hidden;
    box-shadow: 0 6px 18px rgba(0,0,0,0.25);
  }

  /* Front */
  .card-front {
    left: 40px; top: 80px;
    background: linear-gradient(to bottom, var(--card-blue) 0%, var(--card-blue) 48%, #1446a8 72%, var(--card-deep) 100%);
  }
  .front-name {
    position: absolute; left: 66px; top: 112px;
    font-family: "Audiowide", sans-serif;
    font-size: 34px; letter-spacing: 3px;
    color: var(--silver);
    white-space: nowrap;
  }
  .front-name .suffix { font-size: 18px; letter-spacing: 1px; }
  .front-truck {
    position: absolute; left: 230px; top: 190px;
    width: 470px; height: 230px;
    background: linear-gradient(to bottom, var(--truck-light) 0%, #3d5fb0 45%, var(--truck-dark) 80%, rgba(5,10,26,0) 100%);
    border-radius: 10px 0 0 0;
    opacity: 0.85;
  }

  /* Back */
  .card-back {
    left: 430px; top: 560px;
    background: var(--card-blue);
  }
  .back-company {
    position: absolute; left: 24px; top: 8px;
    font-family: "Exo 2", sans-serif; font-weight: 700;
    font-size: 21px; color: var(--white); letter-spacing: 0.5px;
  }
  .back-truck {
    position: absolute; left: 0; top: 90px;
    width: 255px; height: 320px;
    background: linear-gradient(to bottom, #9fb6ee 0%, #3e63c4 40%, var(--truck-dark) 100%);
  }
  .person {
    position: absolute; left: 318px; top: 134px; width: 316px;
    font-family: "Josefin Sans", sans-serif;
  }
  .person-name {
    font-size: 38px; font-weight: 400; letter-spacing: 1.5px;
    color: var(--ink); text-transform: uppercase; text-align: right;
    white-space: nowrap;
  }
  .person-rule {
    display: block; width: 234px; height: 4px;
    background: var(--white); margin-top: 6px;
  }
  .person-role {
    text-align: right; margin-top: -14px;
    font-size: 25px; color: var(--white); letter-spacing: 1px;
  }
  .contact {
    position: absolute; left: 316px; top: 248px;
    font-family: "Josefin Sans", sans-serif; font-weight: 300;
    font-size: 17px; line-height: 23px; letter-spacing: 0.5px; color: var(--ink);
    list-style: none; white-space: nowrap;
  }
  .contact .label { display: inline-block; width: 66px; }
</style>
</head>
<body>
<main class="canvas">

  <section class="card card-front" aria-label="Card front">
    <div class="front-name">BECKLEY HAULAGE<span class="suffix">, INC</span></div>
    <div class="front-truck" role="img" aria-label="Photo of a blue semi truck with a white trailer, seen from the front-left"></div>
  </section>

  <section class="card card-back" aria-label="Card back">
    <div class="back-company">Beckley Haulage, Inc</div>
    <div class="back-truck" role="img" aria-label="Front view photo of a blue semi truck cab"></div>
    <div class="person">
      <div class="person-name">Dale Quimby</div>
      <span class="person-rule"></span>
      <div class="person-role">CEO</div>
    </div>
    <ul class="contact">
      <li>PO BOX 672</li>
      <li>Cedar Flats, NV</li>
      <li><span class="label">Phone</span>: 801-555-0174</li>
      <li><span class="label">Email</span>: beckleyhaulageinc@quillpost.net</li>
    </ul>
  </section>

</main>
</body>
</html>
```